My Insurance Agency Show Display

I need to design a 10 ft x 8 ft backdrop for a show display. This is a pop up fabric most likely display that will be used for a show booth. I need someone to design something more attractive with my logo and make it more flashy so people can see and remember my company. I have attached my rough design so far. I would like it to look more modern. The photo in the design does not have to be used.

This is for an insurance agency that provides Home, Auto, Life and Health products to consumers. We also provide Renters insurance, Commercial, RV, mobile homes, and other products to our customers.

Target Market(s)

Home Owners, and Multiple Auto Owners

Industry/Entity Type

Property and Causality Insurance

Font styles to use
Sans Serif

Colors
0054AA
0677BA
7BADD7
CADEEF
E8F1F8
00AB8E
00BBA5
67D7C9
C6EFE9
E9F9F6

Requirements
Must have
• Attractive Modern Layout
Nice to have
• new and creative. Something that pops with color
Should not have
• Any affiliation to other insurance agencies.

```html
<!DOCTYPE html>
<html lang="en">
<head>
<meta charset="utf-8">
<title>Keel Insurance Agency – Show Backdrop</title>
<link rel="stylesheet" href="https://fonts.googleapis.com/css2?family=League+Spartan:wght@600;700&family=Josefin+Sans:wght@400;500&family=Roboto+Condensed:wght@300;400&family=Montserrat:wght@700;800&display=swap">
<style>
  :root {
    --blue-deep: #0054AA;
    --blue: #0677BA;
    --blue-soft: #7BADD7;
    --blue-pale: #CADEEF;
    --blue-mist: #E8F1F8;
    --teal: #00AB8E;
    --teal-bright: #00BBA5;
    --teal-soft: #67D7C9;
    --teal-pale: #C6EFE9;
    --teal-mist: #E9F9F6;
    --ink: #14233a;
    --paper: #ffffff;
  }
  * { margin: 0; padding: 0; box-sizing: border-box; }
  html, body {
    width: 1200px; height: 840px; overflow: hidden;
    background: var(--paper);
  }
  .backdrop {
    position: relative; width: 1200px; height: 840px;
    background: var(--paper); overflow: hidden;
  }
  .backdrop-shapes { position: absolute; inset: 0; }
  .brand {
    position: absolute; left: 14px; top: 118px; width: 300px;
    font-family: "League Spartan", sans-serif; font-weight: 700;
    color: var(--ink); text-align: center; line-height: 1.05;
  }
  .brand-name { display: block; font-size: 37px; }
  .brand-sub {
    display: flex; align-items: center; justify-content: center; gap: 12px;
    font-size: 25px; letter-spacing: 7px; margin-top: 6px;
  }
  .brand-sub::before, .brand-sub::after {
    content: ""; width: 56px; height: 2px; background: var(--teal);
  }
  .intro {
    position: absolute; left: 14px; top: 222px; width: 540px;
    font-family: "Josefin Sans", sans-serif; font-weight: 500;
    font-size: 26px; line-height: 1.36; color: var(--ink);
  }
  .services {
    position: absolute; left: 14px; top: 350px;
    display: grid; grid-template-columns: 250px 300px; row-gap: 26px;
    list-style: none;
  }
  .service {
    display: flex; align-items: center; height: 48px;
    font-family: "Roboto Condensed", sans-serif; font-weight: 300;
    font-size: 34px; color: var(--ink);
  }
  .service svg { width: 44px; height: 44px; fill: var(--teal); flex: none; }
  .service .divider {
    width: 2px; height: 56px; background: var(--teal);
    margin: 0 6px 0 10px; flex: none;
  }
  .slogan {
    position: absolute; right: 20px; top: 12px; text-align: right;
    color: var(--paper); font-family: "Roboto Condensed", sans-serif;
  }
  .slogan-lead {
    display: block; font-family: "Montserrat", sans-serif; font-weight: 800;
    font-size: 98px; line-height: 1; color: var(--teal-soft); letter-spacing: -1px;
  }
  .slogan-line { display: block; font-weight: 400; font-size: 56px; line-height: 1.1; }
  .slogan-accent { color: var(--teal-soft); }
  .phone {
    position: absolute; left: 16px; bottom: 40px;
    display: flex; align-items: center; gap: 16px;
    font-family: "League Spartan", sans-serif; font-weight: 700;
    font-size: 84px; color: var(--paper); line-height: 1;
  }
  .phone svg { width: 60px; height: 60px; }
</style>
</head>
<body>
<main class="backdrop">
  <svg class="backdrop-shapes" viewBox="0 0 1200 840" aria-hidden="true">
    <defs>
      <linearGradient id="blueFade" x1="0" x2="1">
        <stop offset="0" stop-color="#0054AA"/>
        <stop offset="1" stop-color="#0677BA"/>
      </linearGradient>
      <linearGradient id="paperShade" x1="0" x2="1">
        <stop offset="0" stop-color="#E8F1F8"/>
        <stop offset="0.5" stop-color="#ffffff"/>
      </linearGradient>
    </defs>
    <rect class="paper-shade" width="1200" height="840" fill="url(#paperShade)"/>
    <polygon class="accent-stripe" points="330,0 360,0 620,255 605,265" fill="#00AB8E"/>
    <polygon class="head-panel" points="378,0 1200,0 1200,392 1010,250 862,300 680,310" fill="url(#blueFade)"/>
    <polygon class="accent-stripe" points="1030,268 1200,375 1200,405 1030,295" fill="#00BBA5"/>
    <circle class="feature-disc" cx="860" cy="560" r="185" fill="#C6EFE9"/>
    <circle class="feature-ring" cx="860" cy="560" r="215" fill="none" stroke="#00AB8E" stroke-width="1.5"/>
    <polygon class="accent-stripe" points="0,680 560,694 0,705" fill="#00BBA5"/>
    <polygon class="foot-panel" points="0,712 560,700 700,786 860,840 0,840" fill="url(#blueFade)"/>
    <polygon class="accent-stripe" points="660,770 860,840 840,840 650,775" fill="#67D7C9"/>
    <polygon class="foot-panel" points="1200,700 1200,840 900,840" fill="url(#blueFade)"/>
    <polygon class="accent-stripe" points="1180,690 1200,700 1200,716" fill="#00BBA5"/>
  </svg>

  <div class="brand">
    <span class="brand-name">KEEL INSURANCE</span>
    <span class="brand-sub">AGENCY</span>
  </div>

  <p class="intro">Trust in our expertise to navigate the complexities of insurance &amp; secure a brighter future for you &amp; your family</p>

  <ul class="services">
    <li class="service">
      <svg viewBox="0 0 24 24"><path d="M12 3 2 12h3v9h5v-6h4v6h5v-9h3z"/></svg>
      <span class="divider"></span>HOME</li>
    <li class="service">
      <svg viewBox="0 0 24 24"><path d="M11 3h2v1a9 9 0 0 1 9 8H2a9 9 0 0 1 9-8zM11 12h2v7a3 3 0 0 1-6 0h2a1 1 0 0 0 2 0z"/></svg>
      <span class="divider"></span>UMBRELLA</li>
    <li class="service">
      <svg viewBox="0 0 24 24"><path d="M5 11 7 5h10l2 6h1a2 2 0 0 1 2 2v4h-2v2h-3v-2H7v2H4v-2H2v-4a2 2 0 0 1 2-2zm2.5 0h9L15 7H9zM6 13.5a1.3 1.3 0 1 0 0 2.6 1.3 1.3 0 0 0 0-2.6zm12 0a1.3 1.3 0 1 0 0 2.6 1.3 1.3 0 0 0 0-2.6z"/></svg>
      <span class="divider"></span>AUTO</li>
    <li class="service">
      <svg viewBox="0 0 24 24"><path d="M3 11 12 3l9 8h-2v9h-4v-5H9v5H5v-9z"/><rect x="16" y="3" width="2" height="4"/></svg>
      <span class="divider"></span>RENTERS</li>
    <li class="service">
      <svg viewBox="0 0 24 24"><path d="M12 21 3.5 12.5A5 5 0 0 1 12 5.6a5 5 0 0 1 8.5 6.9z"/></svg>
      <span class="divider"></span>LIFE</li>
    <li class="service">
      <svg viewBox="0 0 24 24"><path d="M3 21V6l8-3v18zm10 0V8h8v13zM5 8h2v2H5zm0 4h2v2H5zm0 4h2v2H5zm3-8h2v2H8zm0 4h2v2H8zm0 4h2v2H8zm7-6h2v2h-2zm0 4h2v2h-2z"/></svg>
      <span class="divider"></span>COMMERCIAL</li>
    <li class="service">
      <svg viewBox="0 0 24 24"><circle cx="7" cy="5" r="2.2"/><circle cx="17" cy="5" r="2.2"/><circle cx="12" cy="10" r="1.8"/><path d="M4 8h6v7H9v6H5v-6H4zm10 0h6v7h-1v6h-4v-6h-1zm-4 5h4v4h-1v4h-2v-4h-1z"/></svg>
      <span class="divider"></span>HEALTH</li>
  </ul>

  <h1 class="slogan">
    <span class="slogan-lead">PROTECTING</span>
    <span class="slogan-line">WHAT MATTERS MOST</span>
    <span class="slogan-line">TO <span class="slogan-accent">YOU</span></span>
  </h1>

  <p class="phone">
    <svg viewBox="0 0 24 24" fill="none" stroke="#ffffff" stroke-width="1.4"><path d="M6 2h3l1.5 5-2 1.5a12 12 0 0 0 7 7l1.5-2 5 1.5v3a2 2 0 0 1-2 2A17 17 0 0 1 4 4a2 2 0 0 1 2-2z"/></svg>
    555-210-4873
  </p>
</main>
</body>
</html>
```